The Silver Lantern book cover

To design an e-book and printed cover that will initially be used on Brellow for Quillet.

My website www.thesilverlantern-example.com

Full title
The Silver Lantern - Start your own success journey in '4 simple steps'.
Subtitle: Everything from understanding your subconscious mind to setting out an action plan for your future.

The Silver Lantern part although it's the beginning of the title will be the smaller part, the rest will be the focus.

I want a clean modern feel, take inspiration from the top self-help books currently on Brellow. Clean crisp and bold.

The book is about setting goals and navigating a complicated road of obstacles in order to achieve them. If this can be illustrated in the graphic or on the cover that would be a bonus.

Requirements for the size of your cover art must have an ideal height/width ratio of at least 1.6, meaning:

• A minimum of 625 pixels on the shortest side and 1000 pixels on the longest side
• For best quality, your image should be 2500 pixels on the longest side
Updates

Reason: Going to go through last time give feedback and any changes before I pick 3 to get a poll done. Loving the ideas and designs. New designs welcome, please put all emphasis on the subheading 'start your...' Have a great Christmas if you celebrate.

Target Market(s)

Target market would be middle age male and females.

Industry/Entity Type

Moving

Font styles to use
Serif
Sans Serif

Requirements
Must have
• Must have the full title even if it is split.

Author name Dorian Falk
Nice to have
• The photo of author but not sure whether to use it or not.

Graphics like moving roads and suchlike.

```html
<!DOCTYPE html>
<html lang="en">
<head>
<meta charset="utf-8">
<title>The Silver Lantern — Book Cover</title>
<link rel="stylesheet" href="https://fonts.googleapis.com/css2?family=Cinzel:wght@400;600&family=Libre+Baskerville:wght@700&family=Didact+Gothic&display=swap">
<style>
  :root {
    --gold: #f5b91c;
    --white: #ffffff;
    --sky-dark: #37423f;
    --sky-mid: #5d6a52;
    --haze: #b9b79a;
    --road: #7f7f7a;
    --road-dark: #5c5d5a;
  }
  html, body {
    margin: 0;
    padding: 0;
    width: 729px;
    height: 1200px;
    overflow: hidden;
    background: var(--sky-dark);
  }
  .cover {
    position: relative;
    width: 729px;
    height: 1200px;
    overflow: hidden;
  }
  .cover-photo {
    position: absolute;
    inset: 0;
    background:
      radial-gradient(ellipse 260px 150px at 80px 510px, rgba(240,230,120,0.75), rgba(240,230,120,0) 100%),
      radial-gradient(ellipse 520px 260px at 560px 600px, rgba(235,230,200,0.75), rgba(235,230,200,0) 100%),
      linear-gradient(180deg,
        var(--sky-dark) 0%,
        #3f4b45 25%,
        var(--sky-mid) 38%,
        #8a8b55 48%,
        var(--haze) 58%,
        #9e9f86 66%,
        #a6a596 72%,
        var(--road) 82%,
        var(--road-dark) 100%);
  }
  .title {
    position: absolute;
    left: 0;
    right: 0;
    top: 0;
    margin: 0;
    font-family: "Cinzel", serif;
    font-weight: 600;
    color: var(--gold);
    text-align: center;
  }
  .title-line {
    position: absolute;
    left: 0;
    right: 0;
    line-height: 1;
  }
  .title-the {
    top: 72px;
    font-size: 48px;
    letter-spacing: 22px;
    text-indent: 22px;
  }
  .title-silver {
    top: 148px;
    font-size: 74px;
    letter-spacing: 24px;
    text-indent: 24px;
  }
  .title-lantern {
    top: 238px;
    font-size: 60px;
    letter-spacing: 12px;
    text-indent: 12px;
  }
  .title-rule {
    position: absolute;
    top: 258px;
    width: 64px;
    height: 20px;
  }
  .title-rule.left { left: 24px; }
  .title-rule.right { right: 24px; }
  .tagline {
    position: absolute;
    top: 356px;
    left: 0;
    right: 0;
    margin: 0;
    font-family: "Libre Baskerville", serif;
    font-weight: 700;
    font-size: 26px;
    line-height: 36px;
    color: var(--white);
    text-align: center;
  }
  .subtitle-box {
    position: absolute;
    left: 202px;
    top: 697px;
    width: 326px;
    height: 80px;
  }
  .subtitle-frame {
    position: absolute;
    inset: 0;
  }
  .subtitle {
    position: absolute;
    inset: 0;
    margin: 0;
    display: flex;
    align-items: center;
    justify-content: center;
    font-family: "Didact Gothic", sans-serif;
    font-size: 15.5px;
    line-height: 19px;
    color: var(--white);
    text-align: center;
  }
  .author-label {
    position: absolute;
    left: 0;
    right: 0;
    top: 1116px;
    font-family: "Cinzel", serif;
    font-size: 8px;
    line-height: 10px;
    letter-spacing: 5px;
    text-indent: 5px;
    color: var(--white);
    text-align: center;
  }
  .author-name {
    position: absolute;
    left: 0;
    right: 0;
    top: 1136px;
    font-family: "Cinzel", serif;
    font-weight: 600;
    font-size: 22px;
    line-height: 28px;
    letter-spacing: 15px;
    text-indent: 15px;
    color: var(--white);
    text-align: center;
  }
</style>
</head>
<body>
<main class="cover">
  <div class="cover-photo" role="img" aria-label="Motion-blurred photograph of an open road curving into a bright hazy horizon, with a pair of black dress shoes walking on the asphalt"></div>

  <h1 class="title">
    <span class="title-line title-the">THE</span>
    <span class="title-line title-silver">SILVER</span>
    <span class="title-line title-lantern">LANTERN</span>
  </h1>
  <svg class="title-rule left" viewBox="0 0 64 20" aria-hidden="true">
    <g stroke="#f5b91c" stroke-width="2">
      <line x1="8" y1="3" x2="64" y2="3"/>
      <line x1="0" y1="10" x2="64" y2="10"/>
      <line x1="8" y1="17" x2="64" y2="17"/>
    </g>
  </svg>
  <svg class="title-rule right" viewBox="0 0 64 20" aria-hidden="true">
    <g stroke="#f5b91c" stroke-width="2">
      <line x1="0" y1="3" x2="56" y2="3"/>
      <line x1="0" y1="10" x2="64" y2="10"/>
      <line x1="0" y1="17" x2="56" y2="17"/>
    </g>
  </svg>

  <p class="tagline">Start your own success<br>journey in 4 simple steps.</p>

  <div class="subtitle-box">
    <svg class="subtitle-frame" viewBox="0 0 326 80" aria-hidden="true">
      <g fill="none" stroke="#f5b91c" stroke-width="3">
        <polyline points="20,1.5 1.5,1.5 1.5,26"/>
        <polyline points="306,1.5 324.5,1.5 324.5,26"/>
        <polyline points="1.5,54 1.5,78.5 20,78.5"/>
        <polyline points="324.5,54 324.5,78.5 306,78.5"/>
      </g>
    </svg>
    <p class="subtitle">Everything from understanding<br>your subconscious mind to setting<br>out an action plan for your future.</p>
  </div>

  <p class="author-label">AUTHOR:</p>
  <p class="author-name">DORIAN FALK</p>
</main>
</body>
</html>
```